Ledge Crafts one page flyer

We need a standard A4 size flyer for a new company called Ledge Crafts. We are a construction material company and sell trims, crown mouldings, baseboards and panelings.
We would like to see the design with the following information:
1. Size: A4
2. Only one front page, no design need to display on back
3. Logo (Ledge Crafts, see the attached EPS file)
4. Slogan: We offer high quality products for competitive prices.
5. Content please see the PDF file
6. The production has 2 category, one called "Crown Moulding", the other is "Wainscoting", Crown Moulding has 5 productions, wainscoting has 2 production(Details see PDF file)
6. We temporary only can provide low resolution images for 7 productions, only the winner will be provided with High Resolution images.
Look and feel
Each slider illustrates characteristics of the customer's brand and the style your logo design should communicate.

```html
<!DOCTYPE html>
<html lang="en">
<head>
<meta charset="utf-8">
<title>Ledge Crafts – Flyer</title>
<link rel="stylesheet" href="https://fonts.googleapis.com/css2?family=Bebas+Neue&family=Montserrat:wght@400;500;600;700&display=swap">
<style>
:root{
  --blue:#2a5db8;
  --blue-light:#6fa0ee;
  --orange:#f15a29;
  --orange-dark:#d9481b;
  --grey:#5d6670;
  --ink:#222;
  --paper:#f4f4f4;
  --white:#fff;
}
*{margin:0;padding:0;box-sizing:border-box}
html,body{width:869px;height:1200px;overflow:hidden;background:var(--paper)}
body{font-family:"Montserrat",sans-serif;color:var(--ink)}
.flyer{position:relative;width:869px;height:1200px;background:var(--paper);overflow:hidden}
.abs{position:absolute}

/* header */
.header{left:0;top:0;width:869px;height:160px;background:var(--white)}
.header-band{left:183px;top:127px;width:686px;height:32px;background:var(--blue)}
.corner-right{right:0;top:50px}
.brand{left:330px;top:34px;display:flex;align-items:center;gap:18px}
.brand-mark{width:62px;height:62px;background:var(--orange)}
.brand-name{font-size:44px;font-weight:600;letter-spacing:4px;color:var(--grey);line-height:1}
.brand-tagline{left:424px;top:98px;font-size:15px;letter-spacing:3.6px;color:var(--grey);font-weight:400}

/* hero */
.hero{left:0;top:158px;width:869px;height:316px;
  background:linear-gradient(180deg,#7d6d62 0%,#958577 32%,#6b4a33 40%,#7a4e30 70%,#4a2c1a 100%)}
.corner-left{left:0;top:0}

/* slogan */
.slogan{left:0;top:473px;width:869px;height:52px;background:var(--orange);
  font-family:"Bebas Neue",sans-serif;color:var(--white);font-size:42px;line-height:54px;text-align:center;letter-spacing:.3px}
.slogan-tab{left:318px;top:525px;width:233px;height:8px;background:var(--orange);border-radius:0 0 6px 6px}

/* section tags */
.tag{height:33px;color:var(--white);font-size:26px;font-weight:500;line-height:33px;letter-spacing:.5px}
.tag-crown{left:0;top:564px;width:316px;padding-left:20px;background:var(--blue);clip-path:polygon(0 0,96% 0,100% 50%,96% 100%,0 100%)}
.tag-wains{left:624px;top:564px;width:245px;padding-left:24px;background:var(--blue);clip-path:polygon(4% 0,100% 0,100% 100%,4% 100%,0 50%)}
.tag-contact{left:0;top:1049px;width:257px;padding-left:20px;height:35px;line-height:35px;font-size:30px;background:var(--orange);clip-path:polygon(0 0,94% 0,100% 50%,94% 100%,0 100%)}
.divider{left:596px;top:605px;width:1px;height:370px;background:#ddd}

/* product cards */
.product{width:170px;height:190px}
.product svg{position:absolute;left:0;top:0}
.size-pill{position:absolute;left:30px;top:-6px;width:110px;height:30px;border-radius:15px;background:var(--orange);
  color:var(--white);font-size:14px;font-weight:600;text-align:center;line-height:30px;letter-spacing:.5px}
.product-shot{position:absolute;left:45px;top:45px;width:80px;height:62px;border-radius:4px;
  background:linear-gradient(135deg,#1a1a1a 0%,#8a8a8a 50%,#f2f2f2 100%)}
.placeholder-word{position:absolute;left:0;top:68px;width:170px;text-align:center;font-size:11px;font-weight:500}
.product-name{position:absolute;left:-20px;top:124px;width:210px;text-align:center;font-size:11.5px;font-weight:500;line-height:14px;letter-spacing:.3px}

/* footer */
.contact-band{left:0;top:0}
.contact-block{color:var(--white);font-size:9.5px;line-height:20px}
.contact-title{font-size:13px;font-weight:500;text-decoration:underline;text-underline-offset:3px;margin-bottom:4px}
.contact-line{display:flex;align-items:center;gap:5px}
.contact-line svg{flex:none}
.office-title{left:628px;top:1027px;color:var(--white);font-size:24px;font-weight:600;text-decoration:underline;text-underline-offset:4px;text-decoration-thickness:2px}
.office-hours{left:628px;top:1064px;color:var(--white);font-size:13.5px;font-weight:700;line-height:20px}
.office-icon{left:582px;top:1072px}
.appointment{left:589px;top:1132px;color:var(--white);font-family:"Bebas Neue",sans-serif;font-size:40px;line-height:1}
</style>
</head>
<body>
<main class="flyer">

  <!-- hero imagery -->
  <div class="abs hero" role="img" aria-label="Photo of white crown moulding pieces standing on a wooden floor against a brick wall"></div>

  <header>
    <div class="abs header"></div>
    <svg class="abs corner-left" width="360" height="310" viewBox="0 0 360 310" aria-hidden="true">
      <polygon points="0,0 300,0 0,310" fill="var(--blue)"/>
      <polygon points="300,0 322,0 0,330 0,310" fill="var(--blue-light)"/>
    </svg>
    <svg class="abs corner-right" width="110" height="110" viewBox="0 0 110 110" aria-hidden="true">
      <polygon points="110,0 110,110 0,110" fill="var(--blue-light)"/>
    </svg>
    <div class="abs header-band"></div>
    <div class="abs brand">
      <span class="brand-mark"></span>
      <span class="brand-name">LEDGE CRAFTS</span>
    </div>
    <div class="abs brand-tagline">FOR ALL TYPES OF PROJECTS</div>
  </header>

  <div class="abs slogan">WE OFFER HIGH QUALITY PRODUCTS FOR COMPETITIVE PRICES</div>
  <div class="abs slogan-tab"></div>

  <!-- shared arc -->
  <svg width="0" height="0" style="position:absolute" aria-hidden="true">
    <defs>
      <g id="ring">
        <path d="M43.7,144 A72,72 0 1 1 109.6,17.3" fill="none" stroke="var(--orange)" stroke-width="1.4"/>
        <path d="M109.6,17.3 A72,72 0 0 1 144,43.7" fill="none" stroke="var(--orange)" stroke-width="1.4" stroke-dasharray="3 3"/>
        <path d="M140,39 L144,45 L147,38" fill="none" stroke="var(--orange)" stroke-width="1.4"/>
        <path d="M147,50 A72,72 0 0 1 126.3,144" fill="none" stroke="var(--orange)" stroke-width="1.4"/>
      </g>
    </defs>
  </svg>

  <section class="crown">
    <div class="abs tag tag-crown">CROWN MOULDING</div>

    <div class="abs product" style="left:15px;top:635px">
      <svg width="170" height="170"><use href="#ring"/></svg>
      <div class="size-pill">8 7/16"X3/4"</div>
      <div class="product-shot" role="img" aria-label="Profile of Sienna 9 crown moulding"></div>
      <div class="product-name">SIENNA 9<br>CROWN MOULDING</div>
    </div>
    <div class="abs product" style="left:189px;top:635px">
      <svg width="170" height="170"><use href="#ring"/></svg>
      <div class="size-pill">7 3/4"X3/4"</div>
      <div class="product-shot" role="img" aria-label="Profile of Sienna 8 crown moulding"></div>
      <div class="product-name">SIENNA 8<br>CROWN MOULDING</div>
    </div>
    <div class="abs product" style="left:359px;top:635px">
      <svg width="170" height="170"><use href="#ring"/></svg>
      <div class="size-pill">6 1/2"X3/4"</div>
      <div class="product-shot" role="img" aria-label="Profile of Sienna 7 crown moulding"></div>
      <div class="product-name">SIENNA 7<br>CROWN MOULDING</div>
    </div>
    <div class="abs product" style="left:93px;top:831px">
      <svg width="170" height="170"><use href="#ring"/></svg>
      <div class="size-pill">7 3/4"X3/4"</div>
      <div class="product-shot" role="img" aria-label="Profile of Verona 8 crown moulding"></div>
      <div class="product-name">VERONA 8<br>CROWN MOULDING</div>
    </div>
    <div class="abs product" style="left:281px;top:831px">
      <svg width="170" height="170"><use href="#ring"/></svg>
      <div class="size-pill">6 1/4"X3/4"</div>
      <div class="product-shot" role="img" aria-label="Profile of Verona 6 crown moulding"></div>
      <div class="product-name">VERONA 6<br>CROWN MOULDING</div>
    </div>
  </section>

  <div class="abs divider"></div>

  <section class="wainscoting">
    <div class="abs tag tag-wains">WAINSCOTING</div>
    <div class="abs product" style="left:662px;top:635px">
      <svg width="170" height="170"><use href="#ring"/></svg>
      <div class="size-pill">3 1/4"X1"</div>
      <div class="placeholder-word">IMAGE</div>
      <div class="product-name">COLONIAL<br>CHAIR RAIL</div>
    </div>
    <div class="abs product" style="left:662px;top:829px">
      <svg width="170" height="170"><use href="#ring"/></svg>
      <div class="size-pill">1 3/4"X5/8"</div>
      <div class="placeholder-word">IMAGE</div>
      <div class="product-name">COLONIAL<br>PANEL MOULD</div>
    </div>
  </section>

  <footer>
    <div class="abs tag tag-contact">CONTACT US</div>
    <svg class="abs contact-band" width="869" height="1200" viewBox="0 0 869 1200" aria-hidden="true">
      <polygon points="0,1104 480,1104 560,1200 0,1200" fill="var(--blue)"/>
      <polygon points="582,997 869,997 869,1200 569,1200 497,1097" fill="var(--orange)"/>
      <polyline points="578,1004 506,1097 574,1194" fill="none" stroke="var(--white)" stroke-width="2"/>
    </svg>

    <div class="abs contact-block" style="left:22px;top:1119px">
      <div class="contact-title">LEDGE CRAFTS</div>
      <div class="contact-line">
        <svg width="8" height="8" viewBox="0 0 8 8"><circle cx="4" cy="4" r="4" fill="#fff"/><circle cx="4" cy="3.4" r="1.4" fill="var(--blue)"/></svg>
        218 Maple Grove Rd, unit 2, Lakeview, Ontario L5A 1B2
      </div>
      <div class="contact-line">
        <svg width="8" height="8" viewBox="0 0 8 8"><circle cx="4" cy="4" r="4" fill="#fff"/><rect x="2" y="2.6" width="4" height="2.8" fill="var(--blue)"/></svg>
        hello@ledgecrafts.ca
        <svg style="margin-left:16px" width="8" height="8" viewBox="0 0 8 8"><circle cx="4" cy="4" r="4" fill="#fff"/><path d="M2.6,2.2 L3.6,2.2 L4,3.4 L3.4,3.9 Q4,5 4.8,5.2 L5.3,4.6 L6,5.2 L6,6 Q3,6 2.6,2.2Z" fill="var(--blue)"/></svg>
        905-555-0142
      </div>
    </div>
    <div class="abs contact-block" style="left:333px;top:1119px">
      <div class="contact-title">WAREHOUSE</div>
      <div class="contact-line">
        <svg width="8" height="8" viewBox="0 0 8 8"><circle cx="4" cy="4" r="4" fill="#fff"/><circle cx="4" cy="3.4" r="1.4" fill="var(--blue)"/></svg>
        47 Birchfield Ave, Westdale,
      </div>
      <div style="padding-left:13px;margin-top:-6px">ON M4K 1T8</div>
    </div>

    <div class="abs office-title">OFFICE HOURS</div>
    <svg class="abs office-icon" width="40" height="40" viewBox="0 0 40 40" aria-hidden="true" fill="none" stroke="#fff" stroke-width="2">
      <rect x="3" y="7" width="26" height="24" rx="2"/>
      <line x1="3" y1="13" x2="29" y2="13"/>
      <line x1="9" y1="3" x2="9" y2="9"/><line x1="23" y1="3" x2="23" y2="9"/>
      <rect x="8" y="17" width="3" height="3" fill="#fff"/><rect x="14" y="17" width="3" height="3" fill="#fff"/><rect x="8" y="23" width="3" height="3" fill="#fff"/>
      <circle cx="29" cy="29" r="8" fill="var(--orange)"/>
      <polyline points="29,25 29,29 32,31"/>
    </svg>
    <div class="abs office-hours">
      MON - FRI : 7:00AM - 6:00PM<br>
      SATURDAYS : 8:00AM - 4:00PM<br>
      SUNDAYS : Closed
    </div>
    <div class="abs appointment">BY APPOINTMENT ONLY</div>
  </footer>

</main>
</body>
</html>
```